4 Meadowroots - `Brochure Design Project

We have created a range of Natural & Organic Skincare that we plan on selling to the tourists that visit Australia.

We need a DL sized brochure with approx. 8 x pages designed to reflect a high end Natural & Organic skincare range.

The brand is called 'Velvet Dawn' and the range is called '4 Meadowroots'.

The point of difference with our competitors is that each product contains six unique Australian botanicals that have been chosen for their benefits to the skin. I will attach the first draft copy that was written for each product and appears on the packaging.

We also need to make space for a paragraph or two on the background or philosophy behind the ‘4 Meadowroots’ brand. Why we chose these ingredients, why it is important to use natural & organic ingredients that don’t contain the harmful parabens etc.. The design should have images that refer to that fact that the product is uniquely Australian, natural & organic and should draw on the benefits that Australia is perceived as a ‘pure’, ‘clean’ and ‘natural’ environment.

I have also attached the product artwork for your reference – please note that the gold colour is gold foil. We have samples of the printed boxes and they look great. We do not have product photo's yet and will need positionals from you before we do.

We have the following products in the range. All (except the Lip Balm) contain the six Australian botanicals.

1. Lanolin Lip Balm
2. Lanolin Body Cream
3. Lanolin day cream
4. Placenta (plant) Cream
5. Placenta (plant) Serum
6. Collagen Cream
7. Collagen Serum

The featured products are the Placenta and Collagen products. The lanolin products are secondary.

We do not have images of the Lanolin Body cream or Lip balm. Please simply create positionals.

Please let me know if there is anything else you require.

Reason: I am currently away and will be returning to the office on 10th October. Thank you.

Target Market(s)

Customers are paying a premium so the design must reflect this.

Customers that like Natural & Organic products.

We have included gold foil in the packaging to reflect a high end product. We have also included gold foil as a large part of our target marget is Asian, in particula Chinese. In saying this, the design needs to appeal to both Western and Asian customers.

Industry/Entity Type

Environment

Requirements
Nice to have
• Nature images
Beautiful lady images
Lifestyle images

The design should include the above features but at the same time reflect a classy, high end range.

```html
<!DOCTYPE html>
<html lang="en">
<head>
<meta charset="utf-8">
<title>The 6 Botanical Ingredients – 4 Meadowroots by Velvet Dawn</title>
<link href="https://fonts.googleapis.com/css2?family=Caveat:wght@700&family=Roboto:wght@400;700&display=swap" rel="stylesheet">
<style>
  :root {
    --cream: #fdf9ec;
    --gold: #c4a33a;
    --forest: #0d6b3a;
    --heading-green: #1b6a2c;
    --white: #ffffff;
    --black: #000000;
    --fold: rgba(0, 0, 0, 0.08);
  }
  html, body {
    margin: 0;
    padding: 0;
    overflow: hidden;
  }
  body {
    width: 1071px;
    height: 1200px;
    position: relative;
    background: var(--cream);
    font-family: "Roboto", Arial, sans-serif;
  }
  .spread {
    position: absolute;
    inset: 0;
  }
  .side-band {
    position: absolute;
    left: 1027px;
    top: 0;
    width: 44px;
    height: 1140px;
    background: var(--forest);
  }
  .fold-line {
    position: absolute;
    left: 535px;
    top: 0;
    width: 1px;
    height: 1140px;
    background: var(--fold);
  }
  .page-title {
    position: absolute;
    right: 77px;
    top: 42px;
    margin: 0;
    font-family: "Caveat", cursive;
    font-weight: 700;
    font-size: 58px;
    line-height: 1;
    color: var(--heading-green);
    letter-spacing: 0.5px;
  }
  .ingredient {
    position: absolute;
    left: 0;
    width: 1027px;
    height: 159px;
  }
  .ingredient-photo {
    position: absolute;
    left: 0;
    top: 0;
    width: 309px;
    height: 159px;
  }
  .ingredient-panel {
    position: absolute;
    left: 309px;
    top: 0;
    width: 718px;
    height: 159px;
    background: var(--gold);
  }
  .ingredient-name {
    position: absolute;
    left: 40px;
    top: 22px;
    margin: 0;
    font-family: "Caveat", cursive;
    font-weight: 700;
    font-size: 30px;
    line-height: 1;
    color: var(--heading-green);
  }
  .ingredient-text {
    position: absolute;
    left: 40px;
    top: 58px;
    width: 650px;
    margin: 0;
    font-size: 16.5px;
    line-height: 25px;
    color: var(--white);
  }
  .row-1 { top: 111px; }
  .row-2 { top: 277px; }
  .row-3 { top: 444px; }
  .row-4 { top: 610px; }
  .row-5 { top: 776px; }
  .row-6 { top: 942px; }

  .photo-davidson { background: linear-gradient(120deg, #5b5560 0%, #6a3047 40%, #8e2f4a 70%, #c9b9b6 100%); }
  .photo-kakadu { background: linear-gradient(120deg, #8ab04a 0%, #a9cf6a 45%, #7da43e 100%); }
  .photo-rosella { background: linear-gradient(120deg, #5f6b3a 0%, #b3262a 45%, #c93a35 65%, #8a9a50 100%); }
  .photo-rosehip { background: linear-gradient(120deg, #ece7ea 0%, #c7314a 45%, #d9a0ab 75%, #f1eef0 100%); }
  .photo-avocado { background: linear-gradient(120deg, #7e9b34 0%, #d6dc8a 40%, #a56a3a 60%, #c5c9a8 100%); }
  .photo-wheat { background: linear-gradient(120deg, #c4a46a 0%, #e0cb97 45%, #8e7a4d 100%); }

  .page-bar {
    position: absolute;
    left: 0;
    top: 1140px;
    width: 1071px;
    height: 60px;
    background: var(--black);
  }
  .page-label {
    position: absolute;
    top: 12px;
    margin: 0;
    font-weight: 700;
    font-size: 31px;
    line-height: 36px;
    color: var(--white);
    transform: translateX(-50%);
  }
  .page-label-left { left: 277px; }
  .page-label-right { left: 818px; }
</style>
</head>
<body>
<main class="spread">
  <h1 class="page-title">The 6 Botanical Ingredients</h1>

  <section class="ingredient row-1">
    <div class="ingredient-photo photo-davidson" role="img" aria-label="Close-up photo of dark purple Davidson plums with water droplets"></div>
    <div class="ingredient-panel">
      <h2 class="ingredient-name">Davidson Plum</h2>
      <p class="ingredient-text">A native Australian fruit found in the rainforests of Queensland. It contains high levels of anti-oxidants. This provides significant hydration for the skin and strengthens elasticity.</p>
    </div>
  </section>

  <section class="ingredient row-2">
    <div class="ingredient-photo photo-kakadu" role="img" aria-label="Photo of green Kakadu plums"></div>
    <div class="ingredient-panel">
      <h2 class="ingredient-name">Kakadu Plum</h2>
      <p class="ingredient-text">One of the world's richest sources of Vitamin C. The plant is found in Northern Australia. It is used most commonly in skincare to brighten and plump the skin, giving it a youthful appearance.</p>
    </div>
  </section>

  <section class="ingredient row-3">
    <div class="ingredient-photo photo-rosella" role="img" aria-label="Photo of a red rosella hibiscus calyx"></div>
    <div class="ingredient-panel">
      <h2 class="ingredient-name">Rosella Extract</h2>
      <p class="ingredient-text">A native species of hibiscus and high in anti-oxidants. It stimulates a natural, healthy metabolism for optimal skin cell renewal.</p>
    </div>
  </section>

  <section class="ingredient row-4">
    <div class="ingredient-photo photo-rosehip" role="img" aria-label="Photo of frosted red rosehips"></div>
    <div class="ingredient-panel">
      <h2 class="ingredient-name">Organic Rosehip Oil</h2>
      <p class="ingredient-text">Rich in Vitamin E &amp; Omega 3, 6 and 9 essential fatty acids. Your skin will be comforted, deeply moisturised, look vibrant, feeling smooth and soft.</p>
    </div>
  </section>

  <section class="ingredient row-5">
    <div class="ingredient-photo photo-avocado" role="img" aria-label="Photo of a halved avocado with its seed"></div>
    <div class="ingredient-panel">
      <h2 class="ingredient-name">Organic Avocado</h2>
      <p class="ingredient-text">Provides a rich source of Vitamin A, B, D and E. It penetrates the skin evenly and quickly, allowing skin to be smooth and moisturised.</p>
    </div>
  </section>

  <section class="ingredient row-6">
    <div class="ingredient-photo photo-wheat" role="img" aria-label="Photo of golden wheat ears in a field"></div>
    <div class="ingredient-panel">
      <h2 class="ingredient-name">Vitamin E</h2>
      <p class="ingredient-text">A strong anti-oxidant vital in protecting skin cells from UV light, pollution and other elements that can damage the skin. It helps improves overall skin health by deeply penetrating the skin to reduce the appearance of deep wrinkles, dry and cracked skin.</p>
    </div>
  </section>

  <div class="side-band"></div>
  <div class="fold-line"></div>

  <footer class="page-bar">
    <p class="page-label page-label-left">Page 1</p>
    <p class="page-label page-label-right">Page 2</p>
  </footer>
</main>
</body>
</html>
```